vantaline7 - a safety solution for schools

A Amok App for schools needs your help to design some screens. Its important to have a very simple use of the app. The function of the app is very easy, you put the button to trigger the alarm. The app has a message function. So we need 3 howto screens. you find a better description of the project in the briefing-file. If you have any questions just ask. Thanks in advance for the suggestions. Best Regards, Mert

Target Market(s)

Schools

Industry/Entity Type

Security Service

Font styles to use
Sans Serif

Colors

Designer to choose colors to be used in the design.

Requirements
Must have
• Simple, easy to use, look like a security app, trust,

```html
<!DOCTYPE html>
<html lang="de">
<head>
<meta charset="utf-8">
<title>vantaline7 – App Screens</title>
<link rel="stylesheet" href="https://fonts.googleapis.com/css2?family=Montserrat:wght@300;400;500;600;700&display=swap">
<style>
  :root {
    --bg: #e9ecef;
    --blue-top: #1bb7f7;
    --blue-bottom: #1576ee;
    --green-top: #5ad775;
    --green-bottom: #1fae3b;
    --yellow-top: #f8cc22;
    --yellow-bottom: #f5891a;
    --white: #ffffff;
    --ink-blue: #1b78ee;
    --alarm-red: #f0334f;
    --ring-pale: #b9e2fb;
    --icon-green: #3cc55a;
    --photo-green: #7fa860;
    --photo-path: #b7ad9a;
  }
  * { box-sizing: border-box; margin: 0; padding: 0; }
  html, body { width: 1200px; height: 1109px; overflow: hidden; }
  body {
    background: var(--bg);
    font-family: "Montserrat", sans-serif;
    color: var(--white);
    position: relative;
  }
  .screen {
    position: absolute;
    width: 260px;
    height: 520px;
    border-radius: 34px;
    overflow: hidden;
    box-shadow: 0 14px 30px rgba(40, 60, 90, 0.18);
    display: flex;
    flex-direction: column;
    align-items: center;
    padding: 40px 26px 28px;
  }
  .screen--blue { background: linear-gradient(180deg, var(--blue-top), var(--blue-bottom)); }
  .screen--green { background: linear-gradient(180deg, var(--green-top), var(--green-bottom)); }
  .screen--yellow { background: linear-gradient(180deg, var(--yellow-top), var(--yellow-bottom)); }

  .col-1 { left: 32px; } .col-2 { left: 324px; } .col-3 { left: 616px; } .col-4 { left: 908px; }
  .row-1 { top: 24px; } .row-2 { top: 565px; }

  .back-arrow { align-self: flex-start; width: 16px; height: 16px; margin-bottom: 14px; }
  .screen-title { font-size: 15px; font-weight: 600; text-align: center; }
  .module-label { font-size: 14px; font-weight: 600; }
  .module-desc { font-size: 7px; line-height: 1.45; text-align: center; margin-top: 6px; opacity: .92; max-width: 190px; }

  /* splash */
  .splash { justify-content: center; }
  .brand-name { font-size: 22px; font-weight: 700; letter-spacing: .5px; }
  .brand-tagline { font-size: 10px; font-weight: 300; margin-top: 6px; }
  .loading { font-size: 7px; margin-top: 60px; opacity: .85; }

  /* bell button */
  .bell-button {
    width: 134px; height: 134px; border-radius: 50%;
    background: var(--white);
    display: flex; align-items: center; justify-content: center;
    margin: 26px 0;
    box-shadow: 0 10px 24px rgba(10, 60, 140, .25);
  }
  .bell-button--active { background: var(--ring-pale); position: relative; }
  .bell-button--active .alarm-ring { position: absolute; inset: -8px; }

  /* action pills */
  .actions { width: 100%; display: flex; flex-direction: column; gap: 12px; margin-top: auto; }
  .pill {
    height: 38px; border-radius: 19px; background: var(--white);
    display: flex; align-items: center; padding: 0 16px; gap: 14px;
    color: #2a3340; font-size: 11px; font-weight: 500;
    box-shadow: 0 6px 14px rgba(10, 60, 140, .18);
  }
  .pill svg { width: 14px; height: 14px; flex: none; }
  .countdown { color: var(--icon-green); font-weight: 700; font-size: 11px; width: 14px; }

  /* registration */
  .registration-title { align-self: flex-start; font-size: 22px; font-weight: 300; margin-bottom: 26px; }
  .field { width: 100%; border-bottom: 1px solid rgba(255,255,255,.45); padding-bottom: 6px; margin-bottom: 18px; }
  .field-label { font-size: 7px; font-weight: 600; letter-spacing: .6px; display: block; margin-bottom: 6px; }
  .field-value { font-size: 14px; font-weight: 300; min-height: 14px; display: block; }
  .register-button { margin-top: auto; width: 100%; justify-content: space-between; }
  .register-dot { width: 14px; height: 14px; border-radius: 50%; background: var(--icon-green); }

  /* how to */
  .howto-art {
    width: 178px; height: 150px; border-radius: 22px; background: var(--white);
    margin: 26px 0 22px;
    box-shadow: 0 10px 24px rgba(0,0,0,.14);
  }
  .howto-heading { font-size: 9px; font-weight: 700; text-align: center; margin-bottom: 8px; }
  .howto-body { font-size: 8px; line-height: 1.5; text-align: center; opacity: .92; }
  .pager { display: flex; gap: 8px; margin-top: auto; }
  .pager span { width: 6px; height: 6px; border-radius: 50%; background: rgba(255,255,255,.55); }
  .pager span.is-current { background: var(--white); }

  /* notification */
  .screen--photo { padding: 0; }
  .photo-fill {
    position: absolute; inset: 0;
    background: linear-gradient(180deg, #4d7a3e 0%, var(--photo-green) 40%, var(--photo-path) 100%);
  }
  .push-card {
    position: relative; margin: 90px 14px 0; align-self: stretch;
    background: rgba(255,255,255,.82); border-radius: 14px;
    padding: 10px 12px; color: #2a3340;
  }
  .push-meta { display: flex; align-items: center; gap: 6px; font-size: 7px; font-weight: 500; }
  .push-meta .push-time { margin-left: auto; }
  .push-title { font-size: 13px; font-weight: 700; margin-top: 6px; }
  .push-text { font-size: 9px; margin-top: 3px; }
</style>
</head>
<body>

<!-- Splash -->
<section class="screen screen--blue splash col-1 row-1">
  <div class="brand-name">vantaline7</div>
  <div class="brand-tagline">Weil Sicherheit Priorität hat!</div>
  <div class="loading">Loading …</div>
</section>

<!-- Registration -->
<section class="screen screen--blue col-2 row-1">
  <svg class="back-arrow" viewBox="0 0 16 16" fill="none" stroke="#fff" stroke-width="1.6"><path d="M14 8H2M7 3L2 8l5 5"/></svg>
  <h1 class="registration-title">Registration</h1>
  <div class="field"><span class="field-label">NAME</span><span class="field-value">Lindqvist</span></div>
  <div class="field"><span class="field-label">VORNAME</span><span class="field-value"></span></div>
  <div class="field"><span class="field-label">E-MAIL-ADRESSE</span><span class="field-value"></span></div>
  <div class="field"><span class="field-label">SCHULE</span><span class="field-value"></span></div>
  <div class="pill register-button"><span>Register</span><span class="register-dot"></span></div>
</section>

<!-- Home -->
<section class="screen screen--blue col-3 row-1">
  <h1 class="screen-title">Schul-Alarm auslösen</h1>
  <div class="bell-button">
    <svg width="62" height="62" viewBox="0 0 64 64" fill="none" stroke="var(--ink-blue)" stroke-width="4" stroke-linejoin="round" stroke-linecap="round"><path d="M18 44V28a14 14 0 0128 0v16l5 5H13z"/><path d="M27 53a5 5 0 0010 0"/></svg>
  </div>
  <div class="actions">
    <div class="pill"><svg viewBox="0 0 16 16" fill="none" stroke="var(--icon-green)" stroke-width="1.4"><path d="M2 3h12v8H6l-4 3z"/></svg>Message</div>
    <div class="pill"><svg viewBox="0 0 16 16"><circle cx="8" cy="8" r="5" fill="var(--icon-green)"/><circle cx="8" cy="8" r="2" fill="#fff"/></svg>Settings</div>
  </div>
</section>

<!-- Demo module – alarm running -->
<section class="screen screen--blue col-4 row-1">
  <div class="module-label">Demo Module</div>
  <p class="module-desc">The function of the app is very easy, you put the button to trigger the alarm. The app has a message function.</p>
  <h1 class="screen-title" style="margin-top:12px">Schul-Alarm auslösen</h1>
  <div class="bell-button bell-button--active">
    <svg class="alarm-ring" viewBox="0 0 150 150" fill="none"><circle cx="75" cy="75" r="71" stroke="var(--alarm-red)" stroke-width="4" stroke-dasharray="250 446" transform="rotate(-60 75 75)" stroke-linecap="round"/></svg>
    <svg width="62" height="62" viewBox="0 0 64 64" fill="none" stroke="var(--alarm-red)" stroke-width="4" stroke-linejoin="round" stroke-linecap="round"><path d="M18 44V28a14 14 0 0128 0v16l5 5H13z"/><path d="M27 53a5 5 0 0010 0"/></svg>
  </div>
  <div class="actions">
    <div class="pill"><span class="countdown">09</span>Alarm abbrechen</div>
    <div class="pill"><svg viewBox="0 0 16 16" fill="none" stroke="var(--icon-green)" stroke-width="1.4"><path d="M2 3h12v8H6l-4 3z"/></svg>Message</div>
    <div class="pill"><svg viewBox="0 0 16 16"><circle cx="8" cy="8" r="5" fill="var(--icon-green)"/><circle cx="8" cy="8" r="2" fill="#fff"/></svg>Settings</div>
  </div>
</section>

<!-- Demo module – idle -->
<section class="screen screen--blue col-1 row-2">
  <div class="module-label">Demo Module</div>
  <p class="module-desc">The function of the app is very easy, you put the button to trigger the alarm. The app has a message function.</p>
  <h1 class="screen-title" style="margin-top:12px">Schul-Alarm auslösen</h1>
  <div class="bell-button">
    <svg width="62" height="62" viewBox="0 0 64 64" fill="none" stroke="var(--ink-blue)" stroke-width="4" stroke-linejoin="round" stroke-linecap="round"><path d="M18 44V28a14 14 0 0128 0v16l5 5H13z"/><path d="M27 53a5 5 0 0010 0"/></svg>
  </div>
</section>

<!-- How to use – registration -->
<section class="screen screen--green col-2 row-2">
  <svg class="back-arrow" viewBox="0 0 16 16" fill="none" stroke="#fff" stroke-width="1.6"><path d="M14 8H2M7 3L2 8l5 5"/></svg>
  <h1 class="screen-title">How to Use</h1>
  <div class="howto-art" role="img" aria-label="Illustration: clipboard with pencil for the registration step"></div>
  <p class="howto-heading">It shows how simple the Registration is</p>
  <p class="howto-body">Enter your name, first name, email address and school once, then the app is ready and keeps you safe every day.</p>
  <div class="pager"><span></span><span class="is-current"></span><span></span></div>
</section>

<!-- How to use – alarm -->
<section class="screen screen--yellow col-3 row-2">
  <svg class="back-arrow" viewBox="0 0 16 16" fill="none" stroke="#fff" stroke-width="1.6"><path d="M14 8H2M7 3L2 8l5 5"/></svg>
  <h1 class="screen-title">How to Use</h1>
  <div class="howto-art" role="img" aria-label="Illustration: hand pressing the alarm bell"></div>
  <p class="howto-heading">It shows how you can trigger an alarm</p>
  <p class="howto-body">Tap the bell button once and the alarm goes straight to the school office and to every teacher on duty.</p>
  <div class="pager"><span></span><span class="is-current"></span><span></span></div>
</section>

<!-- Push notification -->
<section class="screen screen--photo col-4 row-2">
  <div class="photo-fill" role="img" aria-label="Photo: schoolchild with a red backpack walking along a park path"></div>
  <div class="push-card">
    <div class="push-meta">
      <svg width="10" height="10" viewBox="0 0 64 64" fill="none" stroke="var(--ink-blue)" stroke-width="6" stroke-linejoin="round"><path d="M18 44V28a14 14 0 0128 0v16l5 5H13z"/></svg>
      <span>Pushnotification Demo</span><span class="push-time">Now</span>
    </div>
    <div class="push-title">Sekretariat</div>
    <div class="push-text">Bitte bleiben Sie wo Sie sind</div>
  </div>
</section>

</body>
</html>
```